A label design for a home grow mushroom kit

Design a label for our home grow mushroom kit. The packaging is a black plastic bucket. We supply the raw materials and start the growing process for growing your own mushrooms at home. When the consumer buys the product the mushrooms will already be growing. They will get 2-4 crops of white mushrooms (button and flat mushrooms)

Our target market is primarily adults that are interested in gardening, growing products etc. We would also like the product to be attractive to kids to learn to grow the product and have fun in doing so (perhaps a mushroom cartoon character would be a good idea)

The name of the product is not confirmed. Our company name is Dunmore Mushrooms. Maybe Dunmore Mushrooms Grow Kits or something along those lines. Doesn't necessarily need to say Dunmore Mushrooms in the title as we can add our logo also.

Image of packaging, and 2 of our company logos attached
Designer to choose colours

Target Market(s)

Adults interested in gardening, home growing etc. Health conscious consumer. Kids for learning to grow

Colors

Designer to choose colors to be used in the design.

Requirements
Must have
• Fun design
Nice to have
• Mushroom character (cartoon etc)

```html
<!DOCTYPE html>
<html lang="en">
<head>
<meta charset="utf-8">
<title>Dunmore Mushrooms Grow Kits – Bucket Label</title>
<link rel="stylesheet" href="https://fonts.googleapis.com/css2?family=Lobster&family=Oswald:wght@500;600&family=Lato:ital,wght@0,400;1,700&display=swap">
<style>
  :root {
    --stage: #232323;
    --frame: #4b3f1b;
    --panel-light: #ffffff;
    --panel-edge: #e0e0e0;
    --brand-brown: #4a3d1c;
    --brand-green: #3c7b46;
    --title-red: #e0433a;
    --ink: #161616;
    --cap-red: #e0564a;
    --stem-cream: #efe3b4;
    --soil: #c98a3c;
    --grass: #7cbf4a;
    --badge-cream: #f1ece0;
  }
  * { margin: 0; padding: 0; box-sizing: border-box; }
  html, body { width: 1200px; height: 684px; overflow: hidden; background: var(--stage); }
  .stage { width: 1200px; height: 684px; display: flex; align-items: center; justify-content: center; }
  .label { width: 591px; height: 620px; display: block; }
  .brand-name { font-family: "Oswald", sans-serif; font-weight: 600; fill: var(--brand-brown); }
  .title-script { font-family: "Lobster", cursive; fill: var(--title-red); }
  .title-main { font-family: "Oswald", sans-serif; font-weight: 600; fill: var(--brand-brown); }
  .title-sub { font-family: "Oswald", sans-serif; font-weight: 500; fill: var(--ink); }
  .blurb { font-family: "Lato", sans-serif; font-style: italic; font-weight: 700; font-size: 34px; fill: var(--ink); }
  .web { font-family: "Lato", sans-serif; font-size: 22px; letter-spacing: 9px; fill: var(--ink); }
</style>
</head>
<body>
<main class="stage">
  <svg class="label" viewBox="-25 -25 1065 1115" xmlns="http://www.w3.org/2000/svg" aria-label="Dunmore Mushrooms Grow Kits label">
    <defs>
      <radialGradient id="panelGlow" cx="0.5" cy="0.62" r="0.6">
        <stop offset="0" stop-color="var(--panel-light)"/>
        <stop offset="1" stop-color="var(--panel-edge)"/>
      </radialGradient>
      <linearGradient id="characterTone" x1="0" y1="0" x2="0" y2="1">
        <stop offset="0" stop-color="var(--cap-red)"/>
        <stop offset="0.4" stop-color="#ec9a80"/>
        <stop offset="0.72" stop-color="var(--stem-cream)"/>
        <stop offset="0.88" stop-color="var(--grass)"/>
        <stop offset="1" stop-color="var(--soil)"/>
      </linearGradient>
      <linearGradient id="badgeTone" x1="0" y1="0" x2="0" y2="1">
        <stop offset="0" stop-color="var(--badge-cream)"/>
        <stop offset="1" stop-color="var(--brand-green)"/>
      </linearGradient>
    </defs>

    <path class="label-shape"
          d="M130,1060 L0,300 Q0,200 100,195 L200,195 Q210,0 520,0 Q820,0 840,195 L915,195 Q1015,200 1015,300 L880,1060 Z"
          fill="url(#panelGlow)" stroke="var(--frame)" stroke-width="34" stroke-linejoin="round"/>

    <g class="brand-lockup">
      <circle cx="330" cy="150" r="36" fill="var(--brand-green)"/>
      <text class="brand-name" x="390" y="185" font-size="96">Dunmore</text>
      <text class="brand-name" x="520" y="255" font-size="44" text-anchor="middle" letter-spacing="3">MUSHROOMS Ltd.</text>
    </g>

    <g class="product-title">
      <text class="title-script" x="130" y="440" font-size="140" textLength="420" lengthAdjust="spacingAndGlyphs">Dunmore</text>
      <text class="title-main" x="130" y="570" font-size="150" textLength="500" lengthAdjust="spacingAndGlyphs">MUSHROOMS</text>
      <text class="title-sub" x="135" y="680" font-size="105" textLength="495" lengthAdjust="spacing">GROW KITS</text>
    </g>

    <rect class="mascot" role="img" aria-label="Cartoon mushroom character with a red cap, smiling, standing on grass and soil"
          x="650" y="275" width="300" height="450" rx="60" fill="url(#characterTone)"/>

    <circle class="anniversary-badge" role="img" aria-label="30 years and still growing anniversary badge" cx="270" cy="835" r="112" fill="url(#badgeTone)"/>

    <g class="blurb-copy">
      <text class="blurb" x="420" y="795">Lorem Ipsum is simply</text>
      <text class="blurb" x="420" y="840">dummy text of the printing</text>
      <text class="blurb" x="420" y="885">and typesetting  industry.</text>
    </g>

    <text class="web" x="505" y="1000" text-anchor="middle">www.yourwebsite.com</text>
  </svg>
</main>
</body>
</html>
```